Kellbrook Tutoring Flyer Design

I need a flyer for a new company based in Samford Valley called 'Kellbrook Tutoring'. We specialise in Mathematics tutoring for students from grade 5 up to grade twelve. We currently have a logo that has purple as its major colour. The final design should convey professionalism, compassion and that education is about maximising peoples possibilities,
Updates

Just thought I would let you know that my slogan is "Maximise your possibilities" and my phone number is 0438260917

Thanks.

My current logo doesn't seem to want to upload

Target Market(s)

The two targets are parents of students in grades 5-12 and students in grades 5-12

Industry/Entity Type

Education

Logo Text

Kellbrook Tutoring

Logo styles of interest
Pictorial/Combination Logo
Abstract Logo
Lettermark Logo
Requirements
Must have
• My slogan is "Maximise your possibilities"
my phone number is 0438260917

```html
<!DOCTYPE html>
<html lang="en">
<head>
<meta charset="utf-8">
<title>Kellbrook Tutoring Flyer</title>
<link href="https://fonts.googleapis.com/css2?family=Cinzel:wght@400;500&family=Italianno&family=Jost:wght@400;500;600&display=swap" rel="stylesheet">
<style>
  :root {
    --purple: #5f4c86;
    --purple-deep: #4a2c4f;
    --lavender: #9b8fc4;
    --orange: #f8a34a;
    --grey-light: #e3e4e8;
    --grey-mid: #c9cacf;
    --grey-top: #b5b5b8;
    --ink: #1f1f22;
    --white: #ffffff;
    --black: #000000;
  }
  html, body {
    margin: 0;
    padding: 0;
    width: 933px;
    height: 1200px;
    overflow: hidden;
    background: var(--white);
  }
  .flyer {
    position: relative;
    width: 933px;
    height: 1200px;
    overflow: hidden;
    background: var(--white);
    font-family: "Jost", Arial, sans-serif;
  }
  .top-strip {
    position: absolute; left: 0; top: 0;
    width: 100%; height: 22px;
    background: var(--grey-top);
  }
  .hero-photo {
    position: absolute; left: 0; top: 188px;
    width: 933px; height: 562px;
    background:
      radial-gradient(ellipse at 60% 35%, #d9b79c 0%, #a77a6e 25%, transparent 55%),
      linear-gradient(100deg, #6a3f5c 0%, #8c6470 35%, #b99a8a 60%, #7d5464 85%, #a05466 100%);
  }
  .shapes {
    position: absolute; left: 0; top: 0;
    width: 933px; height: 1200px;
  }
  .brand-mark {
    position: absolute; left: 30px; top: 35px;
    width: 190px; height: 190px;
    border-radius: 50%;
    background: var(--lavender);
  }
  .brand-name {
    position: absolute; left: 566px; top: 100px;
    margin: 0;
    font-family: "Italianno", cursive;
    font-weight: 400;
    font-size: 60px;
    line-height: 1;
    color: var(--ink);
  }
  .slogan {
    position: absolute; left: 66px; top: 556px;
    margin: 0;
    font-family: "Cinzel", Georgia, serif;
    font-weight: 500;
    font-size: 38px;
    line-height: 44px;
    color: var(--white);
    text-align: center;
    letter-spacing: 0.5px;
  }
  .offer {
    position: absolute; left: 439px; top: 664px;
    width: 444px; height: 444px;
    display: flex; flex-direction: column; align-items: center;
    font-family: "Cinzel", Georgia, serif;
    color: var(--white);
    text-align: center;
  }
  .offer-intro {
    margin: 58px 0 0;
    font-size: 34px;
    letter-spacing: 1px;
  }
  .offer-rule {
    width: 390px; height: 2px;
    background: var(--white);
    margin: 18px 0 20px;
  }
  .offer-subject {
    margin: 0;
    font-size: 44px;
    line-height: 48px;
    font-weight: 500;
  }
  .offer-grades {
    margin: 0;
    font-size: 34px;
    line-height: 36px;
  }
  .mission {
    position: absolute; left: 70px; top: 808px;
    width: 380px;
    color: var(--ink);
  }
  .mission-title {
    margin: 0 0 22px;
    font-size: 22px;
    line-height: 25px;
    font-weight: 600;
    color: var(--purple);
  }
  .mission-list {
    list-style: none;
    margin: 0; padding: 0;
    font-size: 22px;
    line-height: 25px;
  }
  .mission-list li {
    position: relative;
    padding-left: 20px;
    margin-bottom: 10px;
  }
  .mission-list li::before {
    content: "";
    position: absolute; left: 0; top: 9px;
    width: 8px; height: 8px;
    border-radius: 50%;
    background: var(--orange);
  }
  .mission-list strong { font-weight: 600; }
  .contact-band {
    position: absolute; left: 0; top: 1068px;
    width: 933px; height: 132px;
    background: var(--black);
  }
  .contact-name {
    position: absolute; left: 70px; top: 38px;
    margin: 0;
    font-family: "Cinzel", Georgia, serif;
    font-size: 30px;
    color: var(--white);
    letter-spacing: 1px;
  }
  .contact-name .lead { font-size: 26px; }
  .contact-phone {
    position: absolute; right: 68px; top: 34px;
    margin: 0;
    font-size: 33px;
    color: var(--orange);
    letter-spacing: 0.5px;
  }
  .contact-email {
    position: absolute; right: 68px; top: 80px;
    margin: 0;
    font-size: 20px;
    color: var(--white);
  }
</style>
</head>
<body>
<main class="flyer">
  <div class="top-strip"></div>

  <div class="hero-photo" role="img" aria-label="Photograph of a smiling student lying among stacks of books and maths worksheets"></div>

  <svg class="shapes" viewBox="0 0 933 1200" aria-hidden="true">
    <defs>
      <clipPath id="hero-clip"><rect x="0" y="188" width="933" height="562"/></clipPath>
    </defs>
    <g clip-path="url(#hero-clip)">
      <circle cx="120" cy="760" r="400" fill="#4a2c4f" opacity="0.55"/>
      <circle cx="-40" cy="300" r="260" fill="#3b2440" opacity="0.35"/>
    </g>
    <rect x="0" y="750" width="933" height="318" fill="#e3e4e8"/>
    <ellipse cx="200" cy="1000" rx="360" ry="170" fill="#eeeff2"/>
    <circle cx="870" cy="790" r="210" fill="#c9cacf"/>
    <circle cx="0" cy="1068" r="76" fill="#b9b9be"/>
    <path d="M0 743 H392 a11 11 0 0 1 0 22 H0 Z" fill="#f8a34a"/>
    <circle cx="661" cy="886" r="238" fill="#ffffff"/>
    <circle cx="661" cy="886" r="224" fill="#f8a34a"/>
  </svg>

  <div class="brand-mark" aria-hidden="true"></div>
  <h1 class="brand-name">Kellbrook Tutoring</h1>

  <p class="slogan">Maximise your<br>possibilities.</p>

  <section class="offer">
    <p class="offer-intro">Specialising in</p>
    <div class="offer-rule"></div>
    <p class="offer-subject">Mathematics<br>Tutoring</p>
    <div class="offer-rule"></div>
    <p class="offer-grades">From grade 5<br>to grade 12</p>
  </section>

  <section class="mission">
    <p class="mission-title">Our mission is to enhance students’ confidence by:</p>
    <ul class="mission-list">
      <li><strong>valuing</strong> the individual</li>
      <li><strong>increasing</strong> each student’s competence</li>
      <li><strong>having fun</strong> while doing it.</li>
    </ul>
  </section>

  <footer class="contact-band">
    <p class="contact-name"><span class="lead">CALL</span> DANIEL MARSH</p>
    <p class="contact-phone">0438 260 917</p>
    <p class="contact-email">kellbrooktutoring@mailhub.com</p>
  </footer>
</main>
</body>
</html>
```